Larkfield Circuitry LLC is a Minneapolis / St Paul and surrounding communities computer repair and service company. It serves residential and small businesses. We work primarily with virus removal, data recovery, system baselines, networking, and new system installation. The site should look clean, professional, and easy to navigate.

This wordpress project must be coded and integrated into a wordpress theme for easy upload and maintenance.
Updates

Designers - Please make sure your design is in a wordpress theme so that It can be uploaded.  

Thank you,

Brin 

Target Market(s)

Residential and Small Business

Industry/Entity Type

Residential

Requirements
Must have
• Site Content
1. Main Page should have photos that scroll across, Business Description, Space to run
“Specials” Ads
a. Intuitive Navigation
2. Additional Pages
a. Blog for Computer Repair Articles
b. Testimonials Page
c. Contact Pages
d. Services Page with the ability to put in pricing
3. The site must be clean and professional.
4. Wordpress Theme

```html
<!DOCTYPE html>
<html lang="en">
<head>
<meta charset="utf-8">
<title>Larkfield Circuitry LLC — Computer Repair</title>
<link href="https://fonts.googleapis.com/css2?family=Tinos:wght@400;700&family=Arimo:wght@400;700&display=swap" rel="stylesheet">
<style>
  :root{
    --header-top:#262626;
    --header-bottom:#4a4a4a;
    --hero-band:#e6e6e6;
    --hero-deep:#1f3f63;
    --hero-mid:#3a78b3;
    --hero-light:#dcdcdc;
    --bar:#7b7b7b;
    --bar-dark:#555555;
    --ink:#2b2b2b;
    --muted:#7a7a7a;
    --button:#cfcfcf;
    --footer:#1d1d1d;
    --footer-line:#3a3a3a;
    --footer-text:#d8d8d8;
    --footer-muted:#6e6e6e;
    --field:#4a4a4a;
    --white:#ffffff;
  }
  *{margin:0;padding:0;box-sizing:border-box}
  html,body{width:847px;height:1200px;overflow:hidden;background:var(--white)}
  body{position:relative;font-family:"Arimo",Arial,sans-serif;color:var(--ink)}

  .site-header{position:absolute;left:0;top:0;width:847px;height:110px;
    background:linear-gradient(var(--header-top),var(--header-bottom))}
  .brand{position:absolute;left:28px;top:26px;display:flex;align-items:center;gap:10px}
  .brand-mark{width:30px;height:30px;background:var(--white)}
  .brand-name{font-family:"Tinos","Times New Roman",serif;font-weight:700;font-size:24px;color:var(--white)}
  .main-nav{position:absolute;right:22px;top:68px;display:flex;gap:11px}
  .main-nav a{font-family:"Tinos","Times New Roman",serif;font-size:17px;color:var(--white);text-decoration:none}

  .hero-band{position:absolute;left:0;top:110px;width:847px;height:470px;background:var(--hero-band)}
  .hero-slide{position:absolute;left:56px;top:107px;width:740px;height:378px;
    background:radial-gradient(ellipse at 40% 45%,var(--hero-mid) 0%,var(--hero-deep) 32%,var(--hero-light) 60%,#f4f4f4 100%)}
  .company-bar{position:absolute;left:56px;top:508px;width:522px;height:48px;
    background:linear-gradient(90deg,var(--bar-dark),var(--bar));display:flex;align-items:center;padding-left:20px;gap:16px}
  .company-bar span{font-family:"Tinos","Times New Roman",serif;font-size:19px;color:var(--white)}
  .slider-dots{position:absolute;left:656px;top:503px;display:flex;gap:14px;align-items:center}
  .dot{width:24px;height:24px;border-radius:50%;background:var(--white)}
  .dot.active{background:#9a9a9a;border:3px solid var(--white)}

  .services{position:absolute;left:59px;top:588px;display:flex}
  .service{width:185px;padding-right:18px}
  .service h2{font-family:"Tinos","Times New Roman",serif;font-weight:400;font-size:19px;color:var(--ink);height:42px;white-space:nowrap}
  .service-body{display:flex;gap:8px}
  .service-body svg{flex:none;margin-top:2px}
  .service-body p{font-size:9.5px;line-height:12.5px;color:var(--muted)}
  .read-more{display:inline-block;margin-top:18px;width:62px;height:18px;border-radius:9px;
    background:var(--button);font-size:8.5px;line-height:18px;text-align:center;color:#8a8a8a}

  .site-footer{position:absolute;left:0;top:823px;width:847px;height:377px;background:var(--footer)}
  .footer-col{position:absolute;top:40px}
  .footer-col h3,.contact-form h3{font-family:"Tinos","Times New Roman",serif;font-weight:400;font-size:19px;color:var(--footer-text);margin-bottom:14px}
  .footer-col ul{list-style:none}
  .footer-col li{font-size:9.5px;color:var(--footer-muted);height:34px;padding-top:4px;border-bottom:1px solid var(--footer-line);width:118px}
  .footer-col.narrow li{width:80px}
  .contact-form{position:absolute;left:524px;top:40px;width:238px}
  .field{display:block;width:238px;height:18px;background:var(--field);margin-bottom:16px;font-size:9px;color:#8d8d8d;padding:4px 6px}
  .field.message{height:76px}
  .submit{display:inline-block;width:54px;height:20px;border-radius:10px;background:var(--white);color:var(--ink);
    font-size:10px;line-height:20px;text-align:center;margin-top:-6px}
  .copyright{position:absolute;left:0;top:310px;width:847px;border-top:1px solid var(--footer-line);
    padding:28px 0 0 20px;font-family:"Tinos","Times New Roman",serif;font-size:13px;color:var(--footer-text)}
</style>
</head>
<body>
  <header class="site-header">
    <div class="brand"><span class="brand-mark"></span><span class="brand-name">Larkfield Circuitry LLC</span></div>
    <nav class="main-nav">
      <a href="#">Home</a><a href="#">Data Recovery</a><a href="#">Services</a><a href="#">Testimonial</a><a href="#">Blog</a><a href="#">Contact Us</a>
    </nav>
  </header>

  <section class="hero-band"></section>
  <div class="hero-slide" role="img" aria-label="Desktop computer with monitor, keyboard and mouse"></div>
  <div class="company-bar">
    <svg width="8" height="12" viewBox="0 0 8 12"><path d="M1 1l5 5-5 5" stroke="#fff" stroke-width="2" fill="none"/></svg>
    <span>Our Company</span>
  </div>
  <div class="slider-dots"><span class="dot"></span><span class="dot active"></span><span class="dot"></span></div>

  <main class="services">
    <article class="service">
      <h2>Our Services</h2>
      <div class="service-body">
        <svg width="22" height="20" viewBox="0 0 22 20"><rect x="1" y="5" width="20" height="13" rx="2" fill="#555"/><rect x="7" y="1" width="8" height="5" rx="1" fill="none" stroke="#555" stroke-width="2"/></svg>
        <p>We remove viruses, tune slow machines and set clean system baselines for home and office computers across the Twin Cities area.</p>
      </div>
      <a class="read-more" href="#">Read More</a>
    </article>
    <article class="service">
      <h2>Data Protection</h2>
      <div class="service-body">
        <svg width="20" height="22" viewBox="0 0 20 22"><rect x="2" y="9" width="16" height="12" rx="2" fill="#555"/><path d="M5 9V6a5 5 0 0110 0v3" stroke="#555" stroke-width="2.5" fill="none"/></svg>
        <p>Firewalls, backups and secure networking keep your files safe. We set up protection that runs quietly in the background every day.</p>
      </div>
      <a class="read-more" href="#">Read More</a>
    </article>
    <article class="service">
      <h2>Data Recovery</h2>
      <div class="service-body">
        <svg width="18" height="22" viewBox="0 0 18 22"><path d="M1 1h11l5 5v15H1z" fill="#555"/><path d="M4 10h10M4 14h10M4 18h7" stroke="#fff" stroke-width="1.5"/></svg>
        <p>Lost photos or failed drives? We recover data from hard disks, memory cards and damaged laptops with careful, proven methods.</p>
      </div>
      <a class="read-more" href="#">Read More</a>
    </article>
    <article class="service">
      <h2>Computer Repair.</h2>
      <div class="service-body">
        <svg width="22" height="22" viewBox="0 0 22 22"><path d="M3 19L12 10" stroke="#555" stroke-width="4" stroke-linecap="round"/><circle cx="15" cy="7" r="5" fill="#555"/><circle cx="17" cy="5" r="2.2" fill="#fff"/></svg>
        <p>Fast repairs for desktops and laptops, plus new system installs. Residential and small business clients get clear, fair pricing.</p>
      </div>
      <a class="read-more" href="#">Read More</a>
    </article>
  </main>

  <footer class="site-footer">
    <div class="footer-col" style="left:59px">
      <h3>Services</h3>
      <ul><li>Virus Removal</li><li>Data Recovery</li><li>Networking</li><li>System Setup</li><li>Baselines</li><li>Pricing</li></ul>
    </div>
    <div class="footer-col" style="left:217px">
      <h3>Blog</h3>
      <ul><li>Speed Up Your PC</li><li>Backup Basics</li><li>Safe Browsing</li><li>Spotting Malware</li><li>Router Tips</li></ul>
    </div>
    <div class="footer-col narrow" style="left:428px">
      <h3>Support</h3>
      <ul><li>FAQ</li><li>Pricing</li><li>Remote Help</li><li>Service Area</li><li>Contact</li></ul>
    </div>
    <form class="contact-form">
      <h3>Contact us</h3>
      <span class="field">Name</span>
      <span class="field">Email</span>
      <span class="field message">Message</span>
      <span class="submit">Submit</span>
    </form>
    <p class="copyright">Larkfield Circuitry Copyrights, All right Reserved.</p>
  </footer>
</body>
</html>
```